A business selling natural soaps online and in farmers markets. I want it to reflect local commerce and natural lifestyle. My colors are olive green and saddle brown. I want the dimensions to be 2.25 x 3.25" with matte finish.

The name of my company is Fernwick Soapery, LLC

Business

```html
<!DOCTYPE html>
<html lang="en">
<head>
<meta charset="utf-8">
<title>Fernwick Soapery, LLC — Business Card</title>
<link href="https://fonts.googleapis.com/css2?family=Arimo:wght@400;700&display=swap" rel="stylesheet">
<style>
  :root {
    --backdrop: #e4e2dd;
    --paper: #f1f0eb;
    --olive: #6b9a3a;
    --olive-soft: #a9c88a;
    --saddle: #a0703f;
    --ink: #363636;
  }
  * { margin: 0; padding: 0; box-sizing: border-box; }
  html, body {
    width: 1200px;
    height: 918px;
    overflow: hidden;
    background: var(--backdrop);
    font-family: "Arimo", Arial, sans-serif;
  }
  .card {
    position: absolute;
    left: 180px;
    top: 219px;
    width: 840px;
    height: 480px;
    background: var(--paper);
    box-shadow: 0 10px 30px rgba(0, 0, 0, 0.12);
    overflow: hidden;
  }
  .vine-art {
    position: absolute;
    left: 0;
    top: 0;
    width: 600px;
    height: 340px;
  }
  .brand-name {
    position: absolute;
    left: 310px;
    top: 150px;
    font-size: 40px;
    line-height: 1;
    font-weight: 700;
    color: var(--saddle);
    letter-spacing: -0.5px;
    white-space: nowrap;
  }
  .role {
    position: absolute;
    left: 310px;
    top: 216px;
    font-size: 15px;
    font-weight: 700;
    color: var(--olive);
    letter-spacing: 0.3px;
  }
  .contact {
    position: absolute;
    left: 310px;
    top: 262px;
    width: 500px;
    font-size: 17px;
    line-height: 1.3;
    color: var(--ink);
    list-style: none;
  }
  .contact .address { margin-bottom: 2px; }
  .contact li { display: flex; align-items: center; gap: 6px; }
  .icon { width: 13px; height: 13px; flex: none; }
</style>
</head>
<body>
  <article class="card">
    <svg class="vine-art" viewBox="0 0 600 340" role="img" aria-label="Green leafy vine illustration curling across the top left of the card">
      <defs>
        <linearGradient id="vineTone" x1="0" y1="1" x2="1" y2="0">
          <stop offset="0" stop-color="var(--olive)" stop-opacity="0.8"/>
          <stop offset="1" stop-color="var(--olive-soft)" stop-opacity="0.6"/>
        </linearGradient>
      </defs>
      <path d="M0 40 C120 20 300 25 470 40 C540 46 590 70 580 100 C570 125 450 118 300 112 C285 113 280 130 280 160 L270 300 C260 330 200 335 150 320 C80 300 20 300 0 310 Z" fill="url(#vineTone)"/>
    </svg>

    <h1 class="brand-name">Fernwick Soapery, LLC</h1>
    <p class="role">PROJECT OWNER</p>

    <ul class="contact">
      <li class="address">14, Willowmere Court, 2nd Cross, 6th main,<br>Elm Colony, Hill Layout, Greenpet, Ashford-560 204</li>
      <li>
        <svg class="icon" viewBox="0 0 12 12" aria-hidden="true">
          <rect width="12" height="12" rx="2" fill="var(--olive)"/>
          <path d="M3.5 2.8c.4-.3.9-.2 1.1.2l.6 1.1c.2.3.1.7-.2.9l-.4.3c.4.9 1 1.5 1.9 1.9l.3-.4c.2-.3.6-.4.9-.2l1.1.6c.4.2.5.7.2 1.1l-.5.6c-.4.4-1 .5-1.5.3C5 8.4 3.6 7 2.8 5c-.2-.5-.1-1.1.3-1.5z" fill="var(--paper)"/>
        </svg>
        90412 578 63
      </li>
      <li>
        <svg class="icon" viewBox="0 0 12 12" aria-hidden="true">
          <rect width="12" height="12" rx="2" fill="var(--olive)"/>
          <rect x="2.5" y="3.5" width="7" height="5" fill="none" stroke="var(--paper)" stroke-width="1"/>
          <path d="M2.5 3.5 6 6.3 9.5 3.5" fill="none" stroke="var(--paper)" stroke-width="1"/>
        </svg>
        info@fernwicksoap.com
      </li>
      <li>
        <svg class="icon" viewBox="0 0 12 12" aria-hidden="true">
          <rect width="12" height="12" rx="2" fill="var(--olive)"/>
          <circle cx="6" cy="6" r="3.3" fill="none" stroke="var(--paper)" stroke-width="1"/>
          <path d="M2.7 6h6.6M6 2.7c-1.6 2-1.6 4.6 0 6.6M6 2.7c1.6 2 1.6 4.6 0 6.6" fill="none" stroke="var(--paper)" stroke-width="0.8"/>
        </svg>
        fernwick.com
      </li>
    </ul>
  </article>
</body>
</html>
```